Business card for STEADYLINE

Please design professional business card for IT consulting firm STEADYLINE INC.
Use logo attached.
Use information from sample tRove business card attached.
replace trove inc with STEADYLINE INC.
as well as troveinc.com with steadyline.example

```html
<!DOCTYPE html>
<html lang="en">
<head>
<meta charset="utf-8">
<title>STEADYLINE – Business Card</title>
<link rel="stylesheet" href="https://fonts.googleapis.com/css2?family=Montserrat:wght@400;500;700;800&display=swap">
<style>
  :root {
    --page-bg: #2e2e2e;
    --card-bg: #1f1f20;
    --white: #ffffff;
    --soft-white: #e6e6e6;
    --blue: #5ec8ec;
    --orange: #f7a02a;
    --purple: #8a48a8;
    --teal: #79d0b6;
  }
  * { box-sizing: border-box; margin: 0; padding: 0; }
  html, body {
    width: 1200px; height: 900px; overflow: hidden;
    background: var(--page-bg);
    font-family: "Montserrat", sans-serif;
  }
  .card {
    position: absolute; left: 75px; top: 150px;
    width: 1050px; height: 600px;
    background: var(--card-bg);
    border-radius: 30px;
    overflow: hidden;
    color: var(--white);
  }
  .wordmark {
    position: absolute; top: 110px; left: 0; width: 100%;
    display: flex; justify-content: center; align-items: center; gap: 22px;
  }
  .wordmark-name {
    font-weight: 700; font-size: 88px; letter-spacing: 0.1em;
    color: var(--white); line-height: 1;
  }
  .wordmark-square { width: 34px; height: 34px; background: var(--teal); }
  .identity { position: absolute; top: 272px; width: 100%; text-align: center; }
  .person-name {
    font-weight: 800; font-size: 34px; letter-spacing: 0.03em; color: var(--blue);
  }
  .person-name .credential { color: var(--orange); }
  .person-title {
    margin-top: 8px; font-weight: 500; font-size: 22px; letter-spacing: 0.08em;
    color: var(--soft-white);
  }
  .details {
    position: absolute; top: 380px; left: 0; width: 100%;
    display: flex; justify-content: center; gap: 30px;
  }
  .company-block { text-align: right; font-size: 20px; line-height: 1.45; color: var(--soft-white); font-style: normal; }
  .company-name { font-weight: 700; color: var(--teal); letter-spacing: 0.04em; }
  .divider { width: 2px; background: var(--blue); opacity: 0.8; }
  .contact-list { list-style: none; font-size: 20px; line-height: 1.45; color: var(--soft-white); }
  .contact-list li { display: flex; align-items: center; gap: 10px; }
  .contact-icon { width: 18px; height: 18px; fill: var(--orange); flex: none; }
  .accent-band { position: absolute; left: 0; bottom: 0; width: 100%; height: 16px; display: flex; }
  .accent-band span { flex: 1; }
  .band-orange { background: var(--orange); }
  .band-blue { background: var(--blue); }
  .band-purple { background: var(--purple); }
  .band-teal { background: var(--teal); }
</style>
</head>
<body>
  <section class="card">
    <div class="wordmark">
      <span class="wordmark-name">STEADYLINE</span>
      <span class="wordmark-square"></span>
    </div>

    <div class="identity">
      <h1 class="person-name">DANIEL VORONOV, <span class="credential">P. ENG.</span></h1>
      <p class="person-title">GENERAL MANAGER</p>
    </div>

    <div class="details">
      <address class="company-block">
        <div class="company-name">STEADYLINE INC.</div>
        <div>1280 Harbor Ridge Rd., Suite 240</div>
        <div>Lakeview, Eastfield</div>
        <div>Z9Z 9Z9, Northland</div>
      </address>
      <div class="divider"></div>
      <ul class="contact-list">
        <li>
          <svg class="contact-icon" viewBox="0 0 24 24"><path d="M7 1h10a2 2 0 0 1 2 2v18a2 2 0 0 1-2 2H7a2 2 0 0 1-2-2V3a2 2 0 0 1 2-2zm0 3v14h10V4zm5 15.5a1.2 1.2 0 1 0 0 2.4 1.2 1.2 0 0 0 0-2.4z"/></svg>
          (555) 014-2290
        </li>
        <li>
          <svg class="contact-icon" viewBox="0 0 24 24"><path d="M6.6 10.8a15.1 15.1 0 0 0 6.6 6.6l2.2-2.2a1 1 0 0 1 1-.25 11.4 11.4 0 0 0 3.6.57 1 1 0 0 1 1 1V20a1 1 0 0 1-1 1A17 17 0 0 1 3 4a1 1 0 0 1 1-1h3.5a1 1 0 0 1 1 1c0 1.25.2 2.45.57 3.6a1 1 0 0 1-.25 1z"/></svg>
          (555) 013-4471 ext.317
        </li>
        <li>
          <svg class="contact-icon" viewBox="0 0 24 24"><path d="M2 5h20v14H2zm2 2v.5l8 5 8-5V7zm0 2.8V17h16V9.8l-8 5z"/></svg>
          dvoronov@steadyline.example
        </li>
        <li>
          <svg class="contact-icon" viewBox="0 0 24 24"><path d="M12 2a10 10 0 1 0 0 20 10 10 0 0 0 0-20zm0 2a8 8 0 0 1 7.7 5.9H16a13 13 0 0 0-1.6-5.5A8 8 0 0 1 12 4zm-2.4.4A13 13 0 0 0 8 9.9H4.3A8 8 0 0 1 9.6 4.4zM4 12h4a14 14 0 0 0 .2 2H4.3A8 8 0 0 1 4 12zm6 0h4a12 12 0 0 1-.2 2h-3.6A12 12 0 0 1 10 12zm6 0h4a8 8 0 0 1-.3 2h-3.9a14 14 0 0 0 .2-2zM4.9 16h3.4a13 13 0 0 0 1.3 3.6A8 8 0 0 1 4.9 16zm5.5 0h3.2a11 11 0 0 1-1.6 3.8 11 11 0 0 1-1.6-3.8zm5.3 0h3.4a8 8 0 0 1-4.7 3.6 13 13 0 0 0 1.3-3.6z"/></svg>
          www.steadyline.example
        </li>
      </ul>
    </div>

    <div class="accent-band">
      <span class="band-orange"></span>
      <span class="band-blue"></span>
      <span class="band-purple"></span>
      <span class="band-teal"></span>
    </div>
  </section>
</body>
</html>
```